Real Estate Investor needs awesome business card design

I invest in real estate, focused on multi-family properties, and I need a business card to hand out to potential partners. I prefer simple, clean designs, but it needs to stand out, so I'd like there to be a bit of red in the design as well.

It should include this information:

Front
Dallin Pecksworth
Real Estate Investor
Direct phone: 502-867-3394
Email: dallinhpecksworth@quillmail.example
Headshot (Picture), I've uploaded a few, just pick the one you think looks best with your design. You can remove the background from the headshot image if it looks better.

Back
The back of the card's design should flow and be congruent with the front. On the back I want to put an inspirational quote or question. There will be different ones depending on the card, so I'll need the original file so I can edit it in the end.

For now, use “The Pessimist Sees Difficulty In Every Opportunity. The Optimist Sees The Opportunity In Every Difficulty.” -Barnaby Ellsworth

Target Market(s)

Investors

Industry/Entity Type

Real Estate

Contact Information for Business Card

Front
Dallin Pecksworth
Real Estate Investor

Back
The back of the card's design should flow and be congruent with the front. On the back I want to put an inspirational quote or question. There will be different ones depending on the card, so I'll need the original file so I can edit it in the end. I've uploaded some EXAMPLES of business cards with quotes on them. Don't copy but feel free to use them as inspiration.

The design will be printed on "ZIB sized" business cards
1039 x 697 pixels
with rounded corners

Font styles to use
Serif
Decorative
Script

Colors
ec1f27

Requirements
Must have
• Headshot, name, and other information in it.
• 1039 x 697 pixels
• Rounded corners
• Clean design that pops. I'm open to see any color background, including black.
• Headshots can be located here: https://www.filecrate.example/sh/8kd2wq7mzt31hvx/BBQTXP4ruf9LmQ0KhcvWx7b?dl=0
Nice to have
• It would be awesome if the design included a personal signature or monogram, but if not I'll get a personal logo developed later and the card redesigned if I think it needs it.
Should not have
• Cluttered design

```html
<!DOCTYPE html>
<html lang="en">
<head>
<meta charset="utf-8">
<title>Dallin Pecksworth – Business Card</title>
<link href="https://fonts.googleapis.com/css2?family=Roboto+Condensed:wght@300;700&family=Francois+One&family=Rubik+Distressed&family=Kaushan+Script&display=swap" rel="stylesheet">
<style>
  :root {
    --page: #e9e4dc;
    --card: #000000;
    --ink: #ffffff;
    --red: #ec1f27;
    --sky: #a9d8ec;
    --photo-dark: #1c2a45;
    --photo-mid: #6f5a55;
    --photo-light: #d9a98f;
  }
  * { margin: 0; padding: 0; box-sizing: border-box; }
  html, body { width: 1200px; height: 999px; overflow: hidden; }
  body { background: var(--page); position: relative; }

  .card {
    position: absolute;
    width: 431px;
    height: 717px;
    background: var(--card);
    border-radius: 30px;
    overflow: hidden;
    box-shadow: 0 6px 14px rgba(0,0,0,0.25);
  }
  .card--front { left: 122px; top: 113px; }
  .card--back  { left: 597px; top: 110px; }

  /* Front */
  .headshot {
    position: absolute;
    left: 0; top: 0;
    width: 323px; height: 307px;
    background: radial-gradient(ellipse at 55% 35%, var(--photo-light) 0%, var(--photo-mid) 38%, var(--photo-dark) 75%);
  }
  .identity {
    position: absolute;
    left: 105px; top: 345px;
    color: var(--ink);
    font-family: "Roboto Condensed", sans-serif;
  }
  .identity__name { font-weight: 700; font-size: 23px; letter-spacing: 0.3px; text-transform: uppercase; }
  .identity__role { font-weight: 300; font-size: 20px; margin-top: 6px; }

  .contact {
    position: absolute;
    left: 357px; top: 112px;
    height: 518px;
    writing-mode: vertical-rl;
    transform: rotate(180deg);
    display: flex;
    align-items: center;
    gap: 12px;
    color: var(--ink);
    font-family: "Roboto Condensed", sans-serif;
    font-weight: 700;
    font-size: 16px;
    letter-spacing: 1.2px;
  }
  .contact__icon { width: 20px; height: 20px; transform: rotate(90deg); }
  .contact__gap { height: 10px; }

  /* Back */
  .quote {
    position: absolute;
    inset: 0;
    font-family: "Francois One", sans-serif;
    color: var(--ink);
  }
  .quote__mark {
    position: absolute;
    color: var(--red);
    font-family: "Francois One", sans-serif;
    font-size: 72px;
    line-height: 1;
  }
  .quote__mark--open { left: 38px; top: 88px; }
  .quote__mark--close { left: 290px; top: 428px; }
  .quote__line {
    position: absolute;
    left: 72px;
    white-space: nowrap;
    font-size: 29px;
    letter-spacing: 2px;
    line-height: 1;
    text-transform: uppercase;
  }
  .quote__word {
    display: inline-block;
    font-family: "Rubik Distressed", sans-serif;
    font-size: 44px;
    letter-spacing: 0;
    line-height: 1;
    transform: scaleX(0.75);
    transform-origin: left center;
  }
  .quote__word--sky { color: var(--sky); }
  .quote__word--red { color: var(--red); }
  .quote__author {
    position: absolute;
    right: 58px; top: 550px;
    color: var(--ink);
    font-family: "Kaushan Script", cursive;
    font-style: normal;
    font-size: 18px;
    letter-spacing: 1px;
    white-space: nowrap;
  }
</style>
</head>
<body>

<section class="card card--front">
  <div class="headshot" role="img" aria-label="Headshot of Dallin Pecksworth in a navy blazer, background removed"></div>

  <div class="identity">
    <div class="identity__name">Dallin Pecksworth</div>
    <div class="identity__role">Real Estate Investor</div>
  </div>

  <div class="contact">
    <svg class="contact__icon" viewBox="0 0 20 20" aria-hidden="true">
      <rect x="5" y="1.5" width="10" height="17" rx="2" fill="none" stroke="#ec1f27" stroke-width="2"/>
      <line x1="5" y1="15" x2="15" y2="15" stroke="#ec1f27" stroke-width="1.5"/>
    </svg>
    <span class="contact__phone">502-867-3394</span>
    <span class="contact__gap"></span>
    <svg class="contact__icon" viewBox="0 0 20 20" aria-hidden="true">
      <rect x="3" y="2" width="14" height="16" fill="none" stroke="#ec1f27" stroke-width="2"/>
      <polyline points="3,2 10,10 17,2" fill="none" stroke="#ec1f27" stroke-width="1.6"/>
      <polyline points="3,18 9,10" fill="none" stroke="#ec1f27" stroke-width="1.6"/>
      <polyline points="17,18 11,10" fill="none" stroke="#ec1f27" stroke-width="1.6"/>
    </svg>
    <span class="contact__email">dallinhpecksworth@quillmail.example</span>
  </div>
</section>

<section class="card card--back">
  <blockquote class="quote">
    <span class="quote__mark quote__mark--open">“</span>
    <span class="quote__line" style="top:110px">The pessimist sees</span>
    <span class="quote__line" style="top:144px"><span class="quote__word quote__word--sky">Difficulty</span></span>
    <span class="quote__line" style="top:200px">In every</span>
    <span class="quote__line" style="top:244px"><span class="quote__word quote__word--red">Opportunity.</span></span>
    <span class="quote__line" style="top:303px">The optimist sees</span>
    <span class="quote__line" style="top:340px">The <span class="quote__word quote__word--red">Opportunity</span></span>
    <span class="quote__line" style="top:395px">In every</span>
    <span class="quote__line" style="top:432px"><span class="quote__word quote__word--sky">Difficulty.</span></span>
    <span class="quote__mark quote__mark--close">”</span>
    <cite class="quote__author">/ Barnaby Ellsworth /</cite>
  </blockquote>
</section>

</body>
</html>
```